Cleaning service website design

We need a new nice web design(logo will be the same) for a new cleaning service Company:

Informations about Company and logo you can take from flyers in attachments.

This is a cleaning service Company which have simple rules and we would like to show that(in checklist form) on website:

- What we do and that we're Cleaning Green

- Why us?

- How much(our pricing is simple)

Also we would like to communicate with clients by some nice/big pictures on website and the most important thing is our phone number and short/fast Freestimate.

Also there should be some space for description about our Company.

Generally all information on main page can be short: about us, about service(what we do), last reviews, tips (for example: Tip of the week) and other can be some introduction to subpage where will be more information.

There will be few subpages like: About us, About our service, Photos(Before and after), Reviews , Tips, FAQ, Contact, Looking for a Job? - most of them will be just text so you can project just one example.

```html
<!DOCTYPE html>
<html lang="en">
<head>
<meta charset="utf-8">
<title>Tidy Nest House Cleaning</title>
<link href="https://fonts.googleapis.com/css2?family=Ubuntu:ital,wght@0,400;0,500;0,700;1,400&display=swap" rel="stylesheet">
<style>
:root{
  --green:#78b82a;
  --green-dark:#4f8a16;
  --blue:#1565b4;
  --ink:#222;
  --muted:#9a9a9a;
  --orange-top:#ffb21e;
  --orange-bot:#ff7700;
  --red:#e2141b;
  --line:#d6d6d6;
  --panel:#fafafa;
}
*{box-sizing:border-box;margin:0;padding:0}
html,body{width:1200px;height:1039px;overflow:hidden;background:#fff;font-family:"Ubuntu",sans-serif;color:var(--ink)}
.page{position:relative;width:1200px;height:1039px}

/* header */
.site-header{position:absolute;left:0;top:0;width:1200px;height:134px;border-bottom:6px solid #e9e9e9}
.brand{position:absolute;left:150px;top:36px;display:flex;align-items:center;gap:10px;z-index:2;line-height:1.2}
.brand-dot{width:34px;height:34px;border-radius:50%;background:var(--green)}
.brand-name{font-size:28px;font-weight:700;color:var(--blue)}
.callout{position:absolute;right:150px;top:14px;text-align:right}
.callout-line{font-size:14px;color:#333}
.callout-line b{font-weight:700}
.callout-phone{display:flex;align-items:center;justify-content:flex-end;gap:6px;font-size:27px;font-weight:700;color:#111;margin-top:2px}
.main-nav{position:absolute;right:150px;top:66px;display:flex;height:68px}
.main-nav a{font-family:"Ubuntu",sans-serif;font-weight:500;font-size:12px;color:#333;text-decoration:none;display:flex;align-items:center;padding:0 16px;text-transform:uppercase;white-space:nowrap}
.main-nav a:last-child{padding-right:0}
.main-nav a.current{background:#f2f2f2;color:var(--green);border-bottom:6px solid var(--green);padding:6px 14px 0}

/* hero */
.hero{position:absolute;left:0;top:134px;width:1200px;height:503px;overflow:hidden;
  background:radial-gradient(ellipse 260px 330px at 830px 300px,#8fa040 0%,rgba(120,150,50,.6) 50%,rgba(0,0,0,0) 100%),
  linear-gradient(180deg,#3e5a22 0%,#5f8a2c 35%,#4f8420 60%,#2f6312 100%)}
.hero-title{position:absolute;left:150px;top:49px;font-size:41px;line-height:1.2;color:#fff;font-weight:400;letter-spacing:.5px}
.hero-title b{font-weight:700}
.hero-sub{position:absolute;left:150px;top:91px;font-size:22px;line-height:1.3;color:#fff;font-weight:500}
.hero-sub .price{color:var(--red);font-size:38px;font-weight:700;text-shadow:0 1px 2px rgba(0,0,0,.4)}
.perks{position:absolute;left:148px;top:148px;list-style:none}
.perks li{display:flex;align-items:center;gap:12px;height:33.5px;font-size:14.5px;color:#fff;text-shadow:0 1px 2px rgba(0,0,0,.5)}
.badge{position:absolute;left:311px;top:272px;width:70px;height:70px;border-radius:50%;background:radial-gradient(circle at 50% 70%,#8fd03a,#f4f8ec 62%);box-shadow:0 2px 6px rgba(0,0,0,.4)}
.cta{position:absolute;left:149px;top:376px;width:247px;height:58px;border-radius:5px;background:linear-gradient(var(--orange-top),var(--orange-bot));display:flex;align-items:center;justify-content:center;gap:12px;color:#fff;font-size:26px;font-weight:500;text-decoration:none}

/* cards */
.card{position:absolute;top:674px;width:288px;height:342px;border:1px solid var(--line);background:var(--panel);box-shadow:0 8px 8px -6px rgba(0,0,0,.25)}
.card-photo{display:block;margin:4px auto 0;width:277px;height:109px}
.card h2{font-size:20px;font-weight:500;color:var(--green);text-align:center;margin-top:12px}
.checklist{list-style:none;margin:16px 0 0 21px}
.checklist li{display:flex;gap:9px;font-size:13.8px;line-height:19px;margin-bottom:9px;color:#333}
.checklist svg{flex:none;margin-top:2px}
.prices{list-style:none;margin:16px 0 0 33px}
.prices li{font-size:14px;color:#333;margin-bottom:10px}
.prices b{font-weight:400;color:var(--green-dark)}
.card-note{font-size:13px;color:#333;margin:16px 20px 0 37px;line-height:17px}
.card-note a{color:var(--blue)}
.card-fine{font-size:11px;font-style:italic;color:#333;margin:14px 0 0 39px}
.estimate h2{margin-top:18px}
.estimate-form{margin:13px 0 0 31px}
.field{display:block;width:225px;height:29px;border:1px solid #cfcfcf;background:#fff;font-size:10.5px;color:var(--muted);padding:0 12px;line-height:27px;margin-bottom:13px;white-space:nowrap;overflow:hidden}
.field-row{display:flex;gap:8px}
.field-row .field{width:108.5px;padding:0 10px;font-size:10px}
.estimate-foot{display:flex;justify-content:space-between;align-items:flex-end;width:225px;margin-top:14px}
.estimate-call{font-size:10.5px;font-weight:700;color:#111}
.estimate-call span{display:block;font-size:19px;color:var(--blue);font-weight:700}
.submit{width:83px;height:27px;border-radius:2px;background:linear-gradient(var(--orange-top),var(--orange-bot));color:#fff;font-size:12.5px;font-weight:500;display:flex;align-items:center;justify-content:center;margin-bottom:4px}
</style>
</head>
<body>
<div class="page">
  <header class="site-header">
    <div class="brand"><span class="brand-dot"></span><span class="brand-name">Tidy Nest</span></div>
    <div class="callout">
      <div class="callout-line"><b>Call Us</b> to arrange your cleaning on</div>
      <div class="callout-phone">
        <svg width="18" height="24" viewBox="0 0 18 24"><path d="M4 1l4 5-3 3c1 4 3 7 6 9l3-2 4 4-3 3C8 23 1 14 1 5z" fill="#1565b4"/></svg>
        555-214-7730
      </div>
    </div>
    <nav class="main-nav">
      <a class="current" href="#">Home</a><a href="#">About Us</a><a href="#">Our Services</a><a href="#">Photos</a><a href="#">Reviews</a><a href="#">Tips</a><a href="#">Careers</a><a href="#">FAQ</a><a href="#">Contact</a>
    </nav>
  </header>

  <section class="hero" role="img" aria-label="Woman in a green dress stretching her arms joyfully in a sunny green meadow">
    <h1 class="hero-title">SIMPLIFY <b>YOUR LIFE</b></h1>
    <p class="hero-sub">and some there House Cleaning from <span class="price">$79</span></p>
    <ul class="perks">
      <li><svg width="24" height="24" viewBox="0 0 24 24"><path d="M2 22C4 10 12 3 23 2c-1 11-8 19-21 20z" fill="#8ccc2c"/></svg>Locally Owned &amp; Operated</li>
      <li><svg width="24" height="24" viewBox="0 0 24 24"><path d="M2 22C4 10 12 3 23 2c-1 11-8 19-21 20z" fill="#8ccc2c"/></svg>Reliable &amp; Affordable</li>
      <li><svg width="24" height="24" viewBox="0 0 24 24"><path d="M2 22C4 10 12 3 23 2c-1 11-8 19-21 20z" fill="#8ccc2c"/></svg>All Supplies Provided</li>
      <li><svg width="24" height="24" viewBox="0 0 24 24"><path d="M2 22C4 10 12 3 23 2c-1 11-8 19-21 20z" fill="#8ccc2c"/></svg>No Contracts</li>
      <li><svg width="24" height="24" viewBox="0 0 24 24"><path d="M2 22C4 10 12 3 23 2c-1 11-8 19-21 20z" fill="#8ccc2c"/></svg>Pet Friendly</li>
      <li><svg width="24" height="24" viewBox="0 0 24 24"><path d="M2 22C4 10 12 3 23 2c-1 11-8 19-21 20z" fill="#8ccc2c"/></svg>Green Cleaning</li>
    </ul>
    <div class="badge"></div>
    <a class="cta" href="#">GET STARTED
      <svg width="30" height="26" viewBox="0 0 30 26"><path d="M1 8h14V1l14 12-14 12v-7H1z" fill="#fff"/></svg>
    </a>
  </section>

  <article class="card" style="left:148px">
    <div class="card-photo" role="img" aria-label="Smiling family with children and a golden dog on a sofa" style="background:linear-gradient(135deg,#a98866,#e8ddd0 45%,#c9b7a0)"></div>
    <h2>What do we clean?</h2>
    <ul class="checklist">
      <li><svg width="17" height="16" viewBox="0 0 17 16"><rect x="1" y="3" width="12" height="12" fill="none" stroke="#4f8a16" stroke-width="1.6"/><path d="M4 8l3 3 9-10" fill="none" stroke="#4f8a16" stroke-width="2.4"/></svg>Thoroughly clean your bathrooms, kitchen, bedrooms and living areas</li>
      <li><svg width="17" height="16" viewBox="0 0 17 16"><rect x="1" y="3" width="12" height="12" fill="none" stroke="#4f8a16" stroke-width="1.6"/><path d="M4 8l3 3 9-10" fill="none" stroke="#4f8a16" stroke-width="2.4"/></svg>Mop or vacuum your floors</li>
      <li><svg width="17" height="16" viewBox="0 0 17 16"><rect x="1" y="3" width="12" height="12" fill="none" stroke="#4f8a16" stroke-width="1.6"/><path d="M4 8l3 3 9-10" fill="none" stroke="#4f8a16" stroke-width="2.4"/></svg>Dust surfaces</li>
      <li><svg width="17" height="16" viewBox="0 0 17 16"><rect x="1" y="3" width="12" height="12" fill="none" stroke="#4f8a16" stroke-width="1.6"/><path d="M4 8l3 3 9-10" fill="none" stroke="#4f8a16" stroke-width="2.4"/></svg>Collect garbage</li>
      <li><svg width="17" height="16" viewBox="0 0 17 16"><rect x="1" y="3" width="12" height="12" fill="none" stroke="#4f8a16" stroke-width="1.6"/><path d="M4 8l3 3 9-10" fill="none" stroke="#4f8a16" stroke-width="2.4"/></svg>Make beds</li>
    </ul>
  </article>

  <article class="card" style="left:455px">
    <div class="card-photo" role="img" aria-label="Family looking together at a laptop at home" style="background:linear-gradient(135deg,#c9b9a2,#f1ebe3 50%,#8e8a80)"></div>
    <h2>Pricing is..simple</h2>
    <ul class="prices">
      <li><b>$79</b> for homes less than 1000 sq ft</li>
      <li><b>$89</b> for homes 1000-1800 sq ft</li>
      <li><b>$99</b> for homes 1800-2600 sq ft</li>
    </ul>
    <p class="card-note">If your home is larger than 2600 sq ft please <a href="#">call for a quote</a></p>
    <p class="card-fine">*rates are for regular service*</p>
  </article>

  <aside class="card estimate" style="left:761px">
    <h2>Quick Free Estimate</h2>
    <form class="estimate-form">
      <span class="field">Name</span>
      <span class="field">E-mail</span>
      <span class="field">Postal Code</span>
      <span class="field">Phone</span>
      <div class="field-row"><span class="field">No. of Bathrooms</span><span class="field">No. of Bedrooms</span></div>
      <div class="estimate-foot">
        <div class="estimate-call">CALL US TODAY<span>555-214-7730</span></div>
        <div class="submit">SUBMIT</div>
      </div>
    </form>
  </aside>
</div>
</body>
</html>
```